Branding for Clear Current Honours program collateral

The Clear Current Honours, hosted by the Flowline Sector Council, are an annual awards program to recognise excellence in the Australian water industry. The awards presentation ceremony is held over a formal luncheon, with a MC and Keynote Speaker. The awards event is a premium experience for business professionals that work in the work sector. It is a corporate business luncheon with management level professionals in attendance. We are seeking branding design elements that we can use on all awards collateral including the website, printed invitation, event program, social media posts etc. The Clear Current Honours are well known in the industry and recognised by its logo and corporate colours (attached). We would like these incorporated into the design.

Target Market(s)

business professionals

Industry/Entity Type

Water Company

Requirements
Must have
• event logo, corporate colours

```html
<!DOCTYPE html>
<html lang="en">
<head>
<meta charset="utf-8">
<title>Clear Current Honours – South Australia</title>
<link rel="stylesheet" href="https://fonts.googleapis.com/css2?family=Montserrat:wght@500;600&family=Lato:wght@400&display=swap">
<style>
  :root {
    --aqua-deep: #12b9e6;
    --aqua-mid: #5fd3f0;
    --aqua-pale: #c9f1fb;
    --wash-white: #ffffff;
    --ink: #000000;
  }
  html, body {
    margin: 0;
    padding: 0;
    width: 1200px;
    height: 675px;
    overflow: hidden;
    background: var(--wash-white);
  }
  .canvas {
    position: relative;
    width: 1200px;
    height: 675px;
    overflow: hidden;
  }
  .water-texture {
    position: absolute;
    inset: 0;
    background:
      radial-gradient(ellipse 55% 70% at 8% 20%, var(--aqua-deep) 0%, rgba(18,185,230,0.75) 40%, rgba(95,211,240,0) 100%),
      linear-gradient(100deg, var(--aqua-mid) 0%, var(--aqua-pale) 40%, var(--wash-white) 70%, var(--wash-white) 100%);
  }
  .title-frame {
    position: absolute;
    left: 0;
    top: 0;
    width: 1200px;
    height: 675px;
  }
  .title-frame path {
    fill: none;
    stroke: var(--ink);
    stroke-width: 6;
  }
  .event-name {
    position: absolute;
    left: 0;
    width: 1200px;
    text-align: center;
    top: 388px;
    margin: 0;
    font-family: "Montserrat", sans-serif;
    font-weight: 500;
    font-size: 66px;
    line-height: 1;
    letter-spacing: 0.02em;
    color: var(--ink);
  }
  .event-tag {
    position: absolute;
    left: 0;
    width: 1200px;
    text-align: center;
    top: 480px;
    font-family: "Montserrat", sans-serif;
    font-weight: 600;
    font-size: 24px;
    line-height: 1;
    letter-spacing: 0.22em;
    color: var(--ink);
  }
  .event-region {
    position: absolute;
    left: 0;
    width: 1200px;
    text-align: center;
    top: 532px;
    font-family: "Lato", sans-serif;
    font-weight: 400;
    font-size: 21px;
    line-height: 1;
    letter-spacing: 0.22em;
    color: var(--ink);
  }
</style>
</head>
<body>
  <main class="canvas">
    <div class="water-texture" role="img" aria-label="Aqua watercolour wash overlaid with a fine white network of connected nodes, fading to white on the right"></div>

    <svg class="title-frame" viewBox="0 0 1200 675" aria-hidden="true">
      <path d="M412 492 H228 V370 H972 V492 H788"/>
    </svg>

    <h1 class="event-name">Clear Current</h1>
    <div class="event-tag">HONOURS</div>
    <div class="event-region">SOUTH AUSTRALIA</div>
  </main>
</body>
</html>
```